Plakat für Hausverwaltung
Zielgruppe
Hausverwaltung
(Verwaltung von Wohn- und Gewerbeimmobilien)
Aufgabenstellung
Es soll ein Werbeplakat werden, Die Inhalte der Dienstleistung und die Firmenfarben kann der Webseite entnommen werden.
Ein guter Werbespruch und ansprechendes Desing ohne viel Schrift.

```html
<!DOCTYPE html>
<html lang="de">
<head>
<meta charset="utf-8">
<title>KWM Hausverwaltung – Plakat</title>
<link rel="stylesheet" href="https://fonts.googleapis.com/css2?family=Montserrat:wght@300;400;600;700&family=Oswald:wght@200;300&display=swap">
<style>
  :root {
    --bg: #e4e2df;
    --paper-light: #d9d6d2;
    --paper-light-2: #c9c5c0;
    --dark: #2a2928;
    --text-light: #e9e6e1;
    --text-muted: #bdb8b0;
    --accent: #a89a80;
    --headline: #6f6a63;
  }
  * { margin: 0; padding: 0; box-sizing: border-box; }
  html, body { width: 1200px; height: 1200px; overflow: hidden; background: var(--bg); }
  body { font-family: "Montserrat", sans-serif; }

  .poster {
    position: absolute; left: 190px; top: 20px;
    width: 820px; height: 1160px;
    background: var(--dark); overflow: hidden;
    box-shadow: 0 12px 30px rgba(0,0,0,.18);
  }
  .hero {
    position: absolute; left: 0; top: 0; width: 820px; height: 440px;
    background: linear-gradient(180deg, var(--paper-light-2), var(--paper-light));
  }
  .hero-photo {
    position: absolute; right: 0; top: 0; width: 520px; height: 440px;
    background: linear-gradient(120deg, #cfcbc6 0%, #8c8178 35%, #2f3a4e 60%, #5a6a80 100%);
  }
  .hero-intro {
    position: absolute; left: 0; top: 0; width: 360px; height: 540px;
    background: linear-gradient(180deg, var(--paper-light-2), var(--paper-light));
  }
  .brand {
    position: absolute; left: 40px; top: 60px; width: 280px;
    font-weight: 400; color: var(--dark); font-size: 13px; line-height: 1.4; letter-spacing: .3px;
  }
  .brand-name { font-size: 22px; letter-spacing: 6px; display: block; }
  .headline {
    position: absolute; left: 40px; top: 320px; width: 300px;
    font-family: "Oswald", sans-serif; font-weight: 200;
    color: var(--headline); font-size: 38px; line-height: 1.15;
  }

  .offers-title {
    position: absolute; left: 40px; top: 572px;
    color: var(--text-light); font-weight: 600; font-size: 34px; line-height: 1.1;
  }
  .strengths { position: absolute; left: 40px; top: 676px; width: 290px; list-style: none; }
  .strength {
    display: flex; flex-direction: column; align-items: center;
    margin-bottom: 12px; color: var(--text-muted);
    font-family: "Oswald", sans-serif; font-weight: 300; font-size: 12px; text-align: center; line-height: 1.2;
  }
  .strength svg { width: 28px; height: 28px; margin-bottom: 4px; stroke: var(--text-muted); fill: none; stroke-width: 1.5; }

  .divider { position: absolute; left: 40px; top: 1004px; width: 290px; height: 1px; background: var(--accent); }
  .contact {
    position: absolute; left: 40px; top: 1018px; width: 290px; font-style: normal;
    color: var(--accent); font-weight: 300; font-size: 14px; text-align: center; line-height: 1.45;
  }
  .contact p + p { margin-top: 6px; }

  .services { position: absolute; left: 372px; top: 462px; width: 420px; }
  .timeline { position: absolute; left: 383px; top: 480px; width: 1px; height: 585px; background: var(--accent); }
  .service { position: relative; padding-left: 36px; margin-bottom: 18px; }
  .service-num {
    position: absolute; left: 0; top: 0; width: 22px; height: 22px; border-radius: 50%;
    background: var(--accent); color: var(--dark); font-size: 11px; font-weight: 700;
    display: flex; align-items: center; justify-content: center;
  }
  .service h2 { color: var(--text-light); font-size: 17px; font-weight: 700; margin-bottom: 6px; line-height: 22px; }
  .service ul { list-style: none; }
  .service li {
    color: var(--text-muted); font-size: 11px; font-weight: 300; line-height: 1.55;
    padding-left: 10px; position: relative;
  }
  .service li::before { content: "•"; position: absolute; left: 0; }
</style>
</head>
<body>
<main class="poster">
  <section class="hero">
    <div class="hero-photo" role="img" aria-label="Teamfoto: drei Mitarbeitende in Business-Kleidung vor Aktenregalen"></div>
  </section>
  <section class="hero-intro">
    <div class="brand"><span class="brand-name">KWM</span>Haus- und Grundstücksverwaltungs GmbH</div>
    <h1 class="headline">Herzlich willkommen bei Ihrer Hausverwaltung im Raum Lahnfeld</h1>
  </section>

  <h2 class="offers-title">Unsere<br>Angebote</h2>
  <ul class="strengths">
    <li class="strength">
      <svg viewBox="0 0 34 34"><path d="M5 17 L17 6 L29 17 M9 14 V29 H25 V14"/></svg>
      Fachliche<br>Erfahrung
    </li>
    <li class="strength">
      <svg viewBox="0 0 34 34"><rect x="5" y="5" width="24" height="24"/><path d="M17 5 V29 M5 17 H29"/></svg>
      Professionelle<br>Beratung
    </li>
    <li class="strength">
      <svg viewBox="0 0 34 34"><circle cx="10" cy="10" r="4"/><circle cx="24" cy="10" r="4"/><path d="M3 28 C3 19 17 19 17 28 M17 28 C17 19 31 19 31 28"/></svg>
      Junges und<br>engagiertes Team
    </li>
    <li class="strength">
      <svg viewBox="0 0 34 34"><path d="M5 9 H29 M7 6 H27 M9 9 V26 M15 9 V26 M21 9 V26 M27 9 V26 M5 29 H29"/></svg>
      Zukunftsfähig<br>&amp; Verantwortungsbewusst
    </li>
  </ul>
  <div class="divider"></div>
  <address class="contact">
    <p>Lindenweg 12<br>35000 Lahnfeld</p>
    <p>info@kwm-lahnfeld.de</p>
    <p>01234 567890</p>
  </address>

  <div class="timeline"></div>
  <section class="services">
    <article class="service">
      <span class="service-num">1</span>
      <h2>Sondereigentumsverwaltung</h2>
      <ul>
        <li>Direkte Vertretung des Eigentümers gegenüber den Mietern</li>
        <li>Durchführung des gesamten Schriftverkehrs</li>
        <li>Vermietung über anerkannte Makler mit Bonitätsprüfung</li>
        <li>Ausarbeitung und Abschluss erprobter Mietverträge</li>
        <li>Durchführung der Wohnungsübergaben</li>
        <li>Überwachung der Miethöhe und Durchführung von Mietanpassungen</li>
        <li>Überwachung der Zahlungseingänge</li>
        <li>Überwachung des gesamten Zahlungsverkehr und Führen Ihres Mietkontos</li>
        <li>Erfassen der Ein- und Ausgaben</li>
        <li>Abrechnung aller Nebenkosten mit den Mietern</li>
        <li>Verwaltung der Mietkautionen</li>
        <li>Erstellung der jährlichen Gesamtabrechnung für den Eigentümer</li>
        <li>Veranlassen notwendiger Reparaturen und Erhaltungsmaßnahmen</li>
        <li>Einleitung von Sofortmaßnahmen in Notfällen.</li>
      </ul>
    </article>
    <article class="service">
      <span class="service-num">2</span>
      <h2>Wohneigentumsverwaltung</h2>
      <ul>
        <li>Verwaltung der gemeinschaftlichen Angelegenheiten</li>
        <li>Erstellung des Wirtschaftsplans</li>
        <li>Erstellung der Jahresberechnung</li>
        <li>Eigentümerversammlung und Niederschrift</li>
        <li>Verwaltung der gemeinschaftlichen Gelder</li>
        <li>Überwachen der Verträge der Gemeinschaft</li>
        <li>Zahlungsverkehr und Buchführung</li>
        <li>Auftragsvergabe gemäß Beschlussfassung</li>
        <li>Sofortmaßnahmen bei dringenden Schadensfällen</li>
        <li>Technische Betreuung des Gemeinschaftseigentums</li>
        <li>Sicherheitseinrichtungen</li>
        <li>Allgemeine Verwaltung mit Behörden und Eigentümern</li>
      </ul>
    </article>
    <article class="service">
      <span class="service-num">3</span>
      <h2>Mietverwaltung</h2>
      <ul>
        <li>Allgemeine Verwaltung</li>
        <li>Kaufmännische Verwaltung</li>
        <li>Technische Betreuung</li>
        <li>Nebenkostenabrechnungsservice</li>
      </ul>
    </article>
  </section>
</main>
</body>
</html>
```